Zielgruppe
Produtkion von Bioeiern. Wir suchen ein Design für eine Eierpappe. Im Focus stehen die Aspekte Regionalität und Bio
Zielgruppe: Endverbraucher
Aufgabenstellung
Nicht zu bunt eher natur und bodenständig.
Es müssen diverse Sigel (Eu -Bio, Verbandlogo und LUV-Sigel) und EAN auf die Pappe.
Es handelt sich um 6er Pappen und 10er Pappen
Vielleicht gibt es auch Vorschläge zu neuen Verpackungen, also nicht die standrad-Eierpappe....
Nicht unbedingt ein Foto mit dem Huhn auf der grünen Wiese. eher in die Richtung Kartoon oder Karikatur.

```html
<!DOCTYPE html>
<html lang="de">
<head>
<meta charset="utf-8">
<title>Bio Eier – Banderole</title>
<link href="https://fonts.googleapis.com/css2?family=Dancing+Script:wght@500;600&family=Lato:wght@400&display=swap" rel="stylesheet">
<style>
  :root {
    --page: #f3f1ec;
    --band-green: #1d6a36;
    --sand: #d8c6a8;
    --carton: #79b565;
    --eu-green: #8cc63f;
    --seal-red: #d2262b;
    --white: #ffffff;
  }
  * { margin: 0; padding: 0; box-sizing: border-box; }
  html, body {
    width: 1200px; height: 829px; overflow: hidden;
    background: var(--page);
  }
  .canvas { position: relative; width: 1200px; height: 829px; }

  .label-band {
    position: absolute; left: 467px; top: 25px;
    width: 266px; height: 780px;
    background: var(--band-green);
  }
  .rooster-illustration {
    position: absolute; left: 38px; top: 34px;
    width: 190px; height: 132px;
  }
  .product-type {
    position: absolute; left: 0; width: 100%; top: 212px;
    text-align: center; color: var(--sand);
    font-family: "Dancing Script", cursive; font-weight: 600;
    font-size: 82px; line-height: 1;
  }
  .product-name {
    position: absolute; left: 0; width: 100%; top: 300px;
    text-align: center; color: var(--sand);
    font-family: "Lato", sans-serif; font-weight: 400;
    font-size: 84px; line-height: 1; letter-spacing: 1px;
  }
  .tagline {
    position: absolute; left: 0; width: 100%; top: 404px;
    text-align: center; color: var(--sand);
    font-family: "Dancing Script", cursive; font-weight: 500;
    font-size: 25px; line-height: 1;
  }
  .viewing-window {
    position: absolute; left: 76px; top: 484px;
    width: 114px; height: 114px;
  }
  .info-panel {
    position: absolute; left: 79px; top: 600px;
    width: 108px; height: 180px;
    background: var(--sand);
    text-align: center; color: var(--band-green);
    font-family: "Lato", sans-serif;
  }
  .pack-count {
    margin-top: 12px;
    font-family: "Dancing Script", cursive; font-weight: 600;
    font-size: 25px; line-height: 1.1;
  }
  .producer-address {
    margin-top: 10px;
    font-size: 16px; line-height: 1.35;
  }
  .seal-organic {
    position: absolute; left: 18px; top: 693px;
  }
  .seal-control {
    position: absolute; left: 199px; top: 684px;
  }
</style>
</head>
<body>
<div class="canvas">
  <div class="label-band">
    <svg class="rooster-illustration" viewBox="0 0 190 132" role="img" aria-label="Illustration eines Hahns auf einem Hügel">
      <rect width="190" height="132" rx="14" fill="var(--sand)"/>
    </svg>

    <div class="product-type">Bio</div>
    <div class="product-name">Eier</div>
    <div class="tagline">frisch aus der Region!</div>

    <svg class="viewing-window" viewBox="0 0 114 114" aria-hidden="true">
      <circle cx="57" cy="57" r="57" fill="var(--carton)"/>
    </svg>

    <div class="info-panel">
      <div class="pack-count">6 Stück</div>
      <div class="producer-address">Adr. Betrieb<br>PLZ<br>Ortschaft</div>
    </div>

    <svg class="seal-organic" width="52" height="36" viewBox="0 0 52 36" role="img" aria-label="Siegel ökologischer Landbau">
      <rect width="52" height="36" fill="var(--eu-green)"/>
    </svg>

    <svg class="seal-control" width="54" height="54" viewBox="0 0 54 54" role="img" aria-label="Kontrollsiegel Haltungsform">
      <circle cx="27" cy="27" r="25" fill="var(--white)" stroke="var(--seal-red)" stroke-width="4"/>
    </svg>
  </div>
</div>
</body>
</html>
```